Cover Design for my E-Book

I'm looking for cover art for my new book project. It's a business book for musicians entering the field of music for advertising. While it's a business book, the tone of the book is casual, easy to understand and tongue in cheek and I am looking for a design that is simple, clean and modern. I would use the following book covers as references of styles that I think convey the right feeling:

Unwind
The Craft Of Routine
Nimble
Upturn by Dwight Calloway
Ethical Pluralism by Harold Brisket

While this direction is a general guide, I am open to being surprised by something very different from the above. I am a musician who worked with creative briefs all the time and I know how maddening they can be to read. I am only now learning how maddening they can be to write. thanks for your help.

Target Market(s)

Music business students, composers and bands

Industry/Entity Type

Business

Requirements
Must have
• Book Title:

Pitching UP - Thriving Across The Present Age Of Licensed Sound

My Name:

Gordon Tavaresco

```html
<!DOCTYPE html>
<html lang="en">
<head>
<meta charset="utf-8">
<title>Pitching UP — Gordon Tavaresco</title>
<link rel="stylesheet" href="https://fonts.googleapis.com/css2?family=Questrial&family=Poiret+One&display=swap">
<style>
  :root {
    --cover-black: #000000;
    --title-white: #ffffff;
    --title-red: #d8213a;
    --line-grey: #b9b2a6;
    --art-dark: #17150f;
    --art-paper: #d9d2bf;
    --art-green: #98a487;
  }
  html, body {
    margin: 0;
    padding: 0;
    width: 708px;
    height: 1200px;
    overflow: hidden;
    background: var(--cover-black);
  }
  .cover {
    position: relative;
    width: 708px;
    height: 1200px;
    background: var(--cover-black);
    overflow: hidden;
  }
  .book-title {
    position: absolute;
    left: 50px;
    top: 134px;
    margin: 0;
    font-family: "Questrial", sans-serif;
    font-weight: 400;
    font-size: 112px;
    line-height: 1;
    letter-spacing: -2px;
    color: var(--title-white);
    white-space: nowrap;
  }
  .book-title .accent {
    color: var(--title-red);
  }
  .line-rig {
    position: absolute;
    left: 0;
    top: 0;
  }
  .subtitle {
    position: absolute;
    right: 330px;
    top: 380px;
    margin: 0;
    font-family: "Poiret One", sans-serif;
    font-size: 36px;
    line-height: 52px;
    color: var(--title-white);
    text-align: right;
  }
  .subtitle span {
    display: block;
    white-space: nowrap;
  }
  .hook-and-roll-art {
    position: absolute;
    left: 30px;
    top: 585px;
    width: 635px;
    height: 405px;
    background: linear-gradient(180deg, var(--art-dark) 0%, var(--art-dark) 55%, var(--art-paper) 72%, var(--art-green) 85%, var(--art-paper) 100%);
  }
  .author {
    position: absolute;
    right: 48px;
    top: 1078px;
    margin: 0;
    font-family: "Questrial", sans-serif;
    font-size: 34px;
    letter-spacing: 0.5px;
    color: var(--title-white);
    text-transform: uppercase;
    white-space: nowrap;
  }
</style>
</head>
<body>
  <main class="cover">
    <h1 class="book-title">Pitching <span class="accent">UP</span></h1>

    <svg class="line-rig" width="708" height="1200" viewBox="0 0 708 1200" aria-hidden="true">
      <circle cx="407" cy="305" r="8" fill="none" stroke="var(--line-grey)" stroke-width="2.5"/>
      <line x1="407" y1="313" x2="407" y2="585" stroke="var(--line-grey)" stroke-width="1.5"/>
    </svg>

    <p class="subtitle">
      <span>Thriving</span>
      <span>Across The Present Age</span>
      <span>Of Licensed Sound</span>
    </p>

    <div class="hook-and-roll-art" role="img" aria-label="Fishing hook holding a roll of banknotes and sheet music tied with a red rubber band"></div>

    <p class="author">Gordon Tavaresco</p>
  </main>
</body>
</html>
```